Teskar Business Cards

We need new Business Cards for our startup. It just launched.It is working in the high-end it-market. Specifically in the cloud area. We are a hybrid cloud company. The company logo is attached. We are a Swiss based company. Information visible on the card is: 1. Logo 2. Company Name: Teskar AG 3. Subtitle: Hybrid Clouds. 3. Name: Lukas Brenner 4. Adress: Holderweg 12a, 8462 Selmtal, Switzerland 5. Email: lukas@teskar.example. 6. Mobile: +41 79 304 62 18. It should be a grey/white design. Similar to the attached logo. It should have class, high-quality but not too much color and no gold used.

I forgot to add my Position. Please use Founder / CEO. thanks lukas

```html
<!DOCTYPE html>
<html lang="en">
<head>
<meta charset="utf-8">
<title>Teskar AG – Business Cards</title>
<link href="https://fonts.googleapis.com/css2?family=Source+Sans+3:wght@300;400;600;700&display=swap" rel="stylesheet">
<style>
  :root {
    --backdrop: #e6e4e1;
    --card-grey: #676767;
    --card-white: #ffffff;
    --ink: #575757;
    --ink-soft: #6a6a6a;
    --brand-light: #ffffff;
    --brand-dark: #6b6b6b;
    --band: #666666;
  }
  * { margin: 0; padding: 0; box-sizing: border-box; }
  html, body {
    width: 1200px; height: 1000px; overflow: hidden;
    background: var(--backdrop);
    font-family: "Source Sans 3", "Myriad Pro", Arial, sans-serif;
  }
  .canvas { position: relative; width: 1200px; height: 1000px; }

  .card {
    position: absolute; left: 265px; width: 665px; height: 396px;
    box-shadow: 0 2px 6px rgba(0,0,0,0.18);
  }
  .card--front { top: 73px; background: var(--card-grey); }
  .card--back { top: 533px; background: var(--card-white); overflow: hidden; }

  .brand-name {
    position: absolute; font-weight: 300; text-transform: uppercase; white-space: nowrap;
  }
  .card--front .brand-name {
    left: 0; right: 0; top: 170px; text-align: center;
    font-size: 42px; letter-spacing: 0.32em; color: var(--brand-light);
    padding-left: 0.32em;
  }
  .card--back .brand-name {
    left: 33px; top: 52px; font-size: 30px; letter-spacing: 0.3em; color: var(--brand-dark);
  }

  .person { position: absolute; left: 33px; top: 172px; color: var(--ink); }
  .person__name { font-size: 18px; font-weight: 700; text-transform: uppercase; line-height: 22px; }
  .person__role { font-size: 16px; font-weight: 400; line-height: 20px; }

  .company { position: absolute; left: 32px; top: 266px; color: var(--ink); }
  .company__name { font-size: 16px; font-weight: 600; line-height: 22px; margin-bottom: 7px; }
  .contact { list-style: none; font-size: 16px; line-height: 20px; }
  .contact li { display: flex; align-items: center; gap: 6px; }
  .contact svg { width: 14px; height: 14px; fill: var(--ink); }

  .tagline {
    position: absolute; left: 370px; width: 260px; top: 211px; text-align: center;
    font-size: 18px; font-weight: 600; color: var(--ink-soft);
  }
  .address {
    position: absolute; left: 355px; width: 300px; top: 296px; text-align: center;
    font-size: 16px; line-height: 20px; color: var(--ink);
  }
  .card__band { position: absolute; left: 0; right: 0; bottom: 0; height: 31px; background: var(--band); }
</style>
</head>
<body>
<main class="canvas">
  <section class="card card--front" aria-label="Card front">
    <div class="brand-name">Teskar</div>
  </section>

  <section class="card card--back" aria-label="Card back">
    <div class="brand-name">Teskar</div>

    <div class="person">
      <p class="person__name">Lukas Brenner</p>
      <p class="person__role">Founder / CEO</p>
    </div>

    <div class="company">
      <p class="company__name">Teskar AG</p>
      <ul class="contact">
        <li>
          <svg viewBox="0 0 24 24" aria-hidden="true"><path d="M6.6 10.8a15.1 15.1 0 0 0 6.6 6.6l2.2-2.2c.3-.3.7-.4 1-.2 1.1.4 2.3.6 3.6.6.6 0 1 .4 1 1V20c0 .6-.4 1-1 1A17 17 0 0 1 3 4c0-.6.4-1 1-1h3.5c.6 0 1 .4 1 1 0 1.3.2 2.5.6 3.6.1.3 0 .7-.2 1z"/></svg>
          +41 79 304 62 18
        </li>
        <li>
          <svg viewBox="0 0 24 24" aria-hidden="true"><path d="M2 5h20v14H2z M2 5l10 8 10-8" fill="none" stroke="#575757" stroke-width="2"/><path d="M2 5h20l-10 8z"/></svg>
          lukas@teskar.example
        </li>
      </ul>
    </div>

    <p class="tagline">Hybrid Clouds</p>
    <p class="address">Holderweg 12a, 8462 Selmtal,<br>Switzerland 5</p>

    <div class="card__band"></div>
  </section>
</main>
</body>
</html>
```